Solace Chiropractic & Acupuncture Business Cards

I need a business card design that feels elevated. I am open to any of the logo designs uploaded. We have two doctors so I'll need to be able to change out the names.

Information:
Marnie Toller D.C., Dipl. Ac. ASA
584 W 12th St, Ste 320
Larkfield, OR 97419
solacegrove.net
541-555-0147
drmarnie@solacegrove.com
Updates

We have designs we like now, we are just trying to choose between top contenders. Thanks for your submissions!

Contact Information for Business Card

noted in description

Requirements
Must have
• ability to edit info if possible
Nice to have
• Please see our website solacegrove.net for our style and colors

```html
<!DOCTYPE html>
<html lang="en">
<head>
<meta charset="utf-8">
<title>Solace Chiropractic &amp; Acupuncture — Business Cards</title>
<link rel="stylesheet" href="https://fonts.googleapis.com/css2?family=Cormorant+Garamond:wght@500&family=Poppins:wght@400;700&display=swap">
<style>
  :root {
    --backdrop: #ece6df;
    --teal-deep: #225a78;
    --teal-soft: #4f8296;
    --navy: #2a3350;
    --ink: #1c1c22;
    --paper: #ffffff;
    --white: #ffffff;
  }
  * { box-sizing: border-box; margin: 0; padding: 0; }
  html, body {
    width: 1200px; height: 800px; overflow: hidden;
    background: var(--backdrop);
  }
  .canvas {
    width: 1200px; height: 800px;
    display: flex; align-items: center; justify-content: center; gap: 44px;
  }
  .card {
    width: 525px; height: 300px;
    border-radius: 4px;
    box-shadow: 0 10px 28px rgba(60, 45, 30, 0.16);
    position: relative; overflow: hidden;
  }

  /* Front */
  .card--front {
    background: linear-gradient(150deg, var(--teal-deep) 0%, var(--teal-soft) 100%);
    display: flex; flex-direction: column; align-items: center; justify-content: center;
  }
  .front-name {
    font-family: "Cormorant Garamond", serif;
    font-weight: 500;
    color: var(--white);
    text-align: center;
    line-height: 1;
  }
  .front-name__word { display: block; font-size: 112px; letter-spacing: 1px; }
  .front-name__line {
    display: block; font-size: 15px; letter-spacing: 1.5px;
    text-transform: uppercase; margin-top: 2px;
  }

  /* Back */
  .card--back {
    background: var(--paper);
    display: flex; align-items: center;
    padding: 0 22px 0 26px;
  }
  .back-name {
    width: 168px; flex: none;
    font-family: "Cormorant Garamond", serif;
    font-weight: 500;
    color: var(--navy);
    text-align: center;
    line-height: 1.1;
  }
  .back-name__word { display: block; font-size: 40px; letter-spacing: 3px; text-transform: uppercase; }
  .back-name__line { display: block; font-size: 15px; letter-spacing: 0.5px; text-transform: uppercase; margin-top: 8px; }
  .divider {
    width: 1.5px; height: 160px; background: var(--navy);
    margin: 0 18px 0 18px; flex: none;
  }
  .details { font-family: "Poppins", sans-serif; color: var(--ink); }
  .details__name { font-weight: 700; font-size: 24px; color: var(--navy); line-height: 1.15; }
  .details__role { font-size: 14px; line-height: 1.3; margin-bottom: 12px; }
  .details__address { font-size: 15px; line-height: 1.3; margin-bottom: 6px; }
  .contact { list-style: none; font-size: 15px; line-height: 1.35; }
  .contact li { display: flex; align-items: center; gap: 6px; white-space: nowrap; }
  .contact svg { width: 13px; height: 13px; flex: none; }
</style>
</head>
<body>
<main class="canvas">
  <section class="card card--front" aria-label="Card front">
    <h1 class="front-name">
      <span class="front-name__word">Solace</span>
      <span class="front-name__line">Chiropractic &amp; Acupuncture</span>
    </h1>
  </section>

  <section class="card card--back" aria-label="Card back">
    <div class="back-name">
      <span class="back-name__word">Solace</span>
      <span class="back-name__line">Chiropractic &amp;<br>Acupuncture</span>
    </div>
    <div class="divider"></div>
    <div class="details">
      <h2 class="details__name">Marnie Toller</h2>
      <p class="details__role">Doctor of Chiropractic<br>Dipl. Ac. ASA</p>
      <p class="details__address">584 W 12th St, Ste 320<br>Larkfield, OR 97419</p>
      <ul class="contact">
        <li>
          <svg viewBox="0 0 24 24" fill="var(--navy)" aria-hidden="true"><path d="M6.6 10.8a15 15 0 0 0 6.6 6.6l2.2-2.2a1 1 0 0 1 1-.25 11.4 11.4 0 0 0 3.6.57 1 1 0 0 1 1 1V20a1 1 0 0 1-1 1A17 17 0 0 1 3 4a1 1 0 0 1 1-1h3.5a1 1 0 0 1 1 1c0 1.25.2 2.45.57 3.57a1 1 0 0 1-.25 1z"/></svg>
          541-555-0147
        </li>
        <li>
          <svg viewBox="0 0 24 24" fill="none" stroke="var(--navy)" stroke-width="2" aria-hidden="true"><circle cx="12" cy="12" r="9"/><path d="M3 12h18M12 3c3 3 3 15 0 18M12 3c-3 3-3 15 0 18"/></svg>
          solacegrove.net
        </li>
        <li>
          <svg viewBox="0 0 24 24" fill="var(--navy)" aria-hidden="true"><path d="M2 11 22 3l-8 20-3-9z"/></svg>
          drmarnie@solacegrove.com
        </li>
      </ul>
    </div>
  </section>
</main>
</body>
</html>
```